brightpath Business Card

Already have the logo, but now need the business card design

Industry/Entity Type

Business Software

Contact Information for Business Card

web site will be brightpath.io / The card should have the person name / position / mobile / email / and company address

Colors

Designer to choose colors to be used in the design.

Requirements
Must have
• See business card details
• One side to have the brightpath logo
Nice to have
• If possible the 'O' from flow can be watermarked into the second side
• Try to fit in the words brightpath Business Solutions

```html
<!DOCTYPE html>
<html lang="en">
<head>
<meta charset="utf-8">
<title>brightpath Business Card</title>
<link rel="stylesheet" href="https://fonts.googleapis.com/css2?family=Roboto:wght@300;400;500;700&display=swap">
<style>
  :root {
    --stage: #2b2c2f;
    --card-white: #ffffff;
    --card-black: #0c0c0d;
    --brand-red: #e3242b;
    --band-grey: #6f7072;
    --ink-dark: #2a2a2c;
    --ink-mid: #4a4a4d;
    --logo-grey: #8d8e91;
    --mark-grey: #dcdcde;
  }
  * { margin: 0; padding: 0; box-sizing: border-box; }
  html, body { width: 1200px; height: 900px; overflow: hidden; }
  body {
    background: var(--stage);
    font-family: "Roboto", Arial, sans-serif;
    display: flex;
    align-items: center;
    justify-content: center;
    gap: 40px;
  }
  .card {
    position: relative;
    width: 540px;
    height: 309px;
    border-radius: 28px;
    overflow: hidden;
    box-shadow: 0 14px 30px rgba(0, 0, 0, 0.35);
  }

  /* Front side */
  .card-front { background: var(--card-white); }
  .identity { position: absolute; left: 40px; top: 34px; }
  .person-name {
    font-size: 24px;
    font-weight: 700;
    letter-spacing: 0.5px;
    color: var(--ink-dark);
    line-height: 1;
  }
  .person-name .first { color: var(--brand-red); }
  .person-role {
    margin-top: 6px;
    font-size: 11px;
    font-weight: 500;
    letter-spacing: 0.6px;
    color: var(--ink-mid);
  }
  .role-rule {
    width: 14px; height: 3px;
    margin-top: 10px;
    background: var(--brand-red);
  }
  .contact-list { list-style: none; margin-top: 12px; }
  .contact-list li {
    display: flex;
    align-items: center;
    gap: 9px;
    font-size: 15px;
    color: var(--ink-dark);
    line-height: 23px;
  }
  .contact-icon { width: 14px; height: 14px; flex: none; }

  .card-mark {
    position: absolute;
    left: 360px; top: 70px;
    width: 140px; height: 140px;
    border-radius: 50%;
    background: var(--mark-grey);
  }

  .footer-band { position: absolute; left: 0; bottom: 0; width: 540px; height: 104px; }
  .tagline {
    position: absolute;
    left: 28px; top: 211px;
    font-size: 15px;
    font-weight: 700;
    letter-spacing: 0.4px;
    color: var(--card-white);
    text-transform: uppercase;
  }
  .address {
    position: absolute;
    left: 28px; top: 262px;
    font-size: 15px;
    font-weight: 400;
    color: var(--card-white);
  }

  /* Back side */
  .card-back {
    background: radial-gradient(ellipse at 30% 20%, #232325 0%, var(--card-black) 70%);
    display: flex;
    align-items: center;
    justify-content: center;
  }
  .brand-wordmark {
    font-size: 76px;
    font-weight: 300;
    letter-spacing: -1px;
    color: var(--logo-grey);
  }
</style>
</head>
<body>

  <section class="card card-front" aria-label="Business card front">
    <div class="identity">
      <h1 class="person-name"><span class="first">MARCUS</span> LANE</h1>
      <p class="person-role">DIRECTOR</p>
      <div class="role-rule"></div>
      <ul class="contact-list">
        <li>
          <svg class="contact-icon" viewBox="0 0 14 14" aria-hidden="true">
            <circle cx="7" cy="7" r="7" fill="#e3242b"/>
            <path d="M4.6 3.6l1.3 1.6-.7.9c.5 1 1.2 1.7 2.2 2.2l.9-.7 1.6 1.3-.8 1.3C6.7 10 4 7.3 3.8 4.4z" fill="#fff"/>
          </svg>
          123 4546 7890
        </li>
        <li>
          <svg class="contact-icon" viewBox="0 0 14 14" aria-hidden="true">
            <circle cx="7" cy="7" r="7" fill="#e3242b"/>
            <rect x="3.5" y="4.5" width="7" height="5" fill="#fff"/>
            <path d="M3.5 4.5L7 7.3l3.5-2.8" fill="none" stroke="#e3242b" stroke-width="0.8"/>
          </svg>
          email@domain.com
        </li>
        <li>
          <svg class="contact-icon" viewBox="0 0 14 14" aria-hidden="true">
            <circle cx="7" cy="7" r="7" fill="#e3242b"/>
            <circle cx="7" cy="7" r="3.6" fill="none" stroke="#fff" stroke-width="0.9"/>
            <path d="M3.4 7h7.2M7 3.4c-1.6 2-1.6 5.2 0 7.2M7 3.4c1.6 2 1.6 5.2 0 7.2" fill="none" stroke="#fff" stroke-width="0.8"/>
          </svg>
          www.brightpath.io
        </li>
      </ul>
    </div>

    <div class="card-mark" aria-hidden="true"></div>

    <svg class="footer-band" viewBox="0 0 540 104" aria-hidden="true">
      <path d="M0 0H282C298 0 302 34 322 34H540V104H0Z" fill="#e3242b"/>
      <rect x="0" y="38" width="540" height="66" fill="#6f7072"/>
    </svg>
    <p class="tagline">brightpath Business Solutions</p>
    <p class="address">412 Orchard Ave. Lakeview, NY 10521</p>
  </section>

  <section class="card card-back" aria-label="Business card back">
    <p class="brand-wordmark">brightpath</p>
  </section>

</body>
</html>
```